SaaS Early tech startup business card design

Unique design for experience ecommerce platform company. the business cards will be used by executive members. conformance with color code is required.

```html
<!DOCTYPE html>
<html lang="en">
<head>
<meta charset="utf-8">
<title>Novra – Executive Business Card</title>
<link rel="stylesheet" href="https://fonts.googleapis.com/css2?family=Poppins:wght@400;500;600;700&family=Michroma&display=swap">
<style>
  :root {
    --page-bg: #1b1b1f;
    --card-navy: #23213a;
    --ink-white: #ffffff;
    --teal: #1fb89c;
    --teal-light: #4fcaa8;
    --blue: #0f6f97;
    --blue-mid: #1289a8;
    --blue-deep: #0c5f86;
  }
  * { box-sizing: border-box; margin: 0; padding: 0; }
  html, body { width: 1200px; height: 900px; overflow: hidden; }
  body {
    background: var(--page-bg);
    font-family: "Poppins", sans-serif;
    position: relative;
  }
  .card {
    position: absolute;
    left: 280px;
    width: 640px;
    height: 366px;
    background: var(--card-navy);
    border-radius: 22px;
    overflow: hidden;
    box-shadow: 0 14px 30px rgba(0,0,0,0.45);
  }
  .card--back { top: 56px; }
  .card--front { top: 478px; }

  /* Back */
  .back-header {
    position: absolute; top: 34px; right: 38px;
    display: flex; align-items: center; gap: 12px;
  }
  .tagline { color: var(--ink-white); font-size: 12px; font-weight: 500; letter-spacing: 0.3px; }
  .header-divider { width: 1px; height: 30px; background: var(--ink-white); opacity: 0.8; }
  .brand-small { color: var(--teal); font-weight: 700; font-size: 34px; line-height: 1; }
  .stat { position: absolute; left: 48px; bottom: 46px; color: var(--ink-white); }
  .stat-figure { font-size: 52px; font-weight: 700; line-height: 1; }
  .stat-text { font-size: 20px; font-weight: 500; line-height: 1.22; margin-top: 6px; }
  .source { position: absolute; right: 40px; bottom: 56px; color: var(--teal); font-size: 11px; font-weight: 600; }

  /* Front */
  .tech-artwork {
    position: absolute; top: 0; right: 0;
    width: 250px; height: 180px;
    background: radial-gradient(ellipse at 75% 0%, rgba(31,184,156,0.30) 0%, rgba(18,137,168,0.18) 45%, rgba(35,33,58,0) 75%);
  }
  .brand-large {
    position: absolute; left: 44px; top: 92px;
    color: var(--teal); font-weight: 700; font-size: 112px; line-height: 1; letter-spacing: -2px;
  }
  .rule { position: absolute; height: 3px; }
  .rule--teal { left: 378px; top: 196px; width: 222px; background: var(--teal); }
  .rule--blue { left: 40px; top: 236px; width: 318px; background: var(--blue); }
  .identity { position: absolute; left: 40px; top: 258px; }
  .person-name { font-family: "Michroma", sans-serif; color: var(--ink-white); font-size: 20px; letter-spacing: 1px; }
  .person-role { font-family: "Michroma", sans-serif; color: var(--blue); font-size: 16px; letter-spacing: 0.5px; margin-top: 2px; }
  .contacts { position: absolute; left: 378px; top: 214px; list-style: none; }
  .contact { display: flex; align-items: center; gap: 10px; color: var(--ink-white); font-family: "Michroma", sans-serif; font-size: 13px; margin-bottom: 8px; }
  .contact-icon { width: 20px; height: 20px; background: var(--blue-mid); display: flex; align-items: center; justify-content: center; border-radius: 2px; }
  .color-band { position: absolute; left: 0; right: 0; bottom: 0; height: 14px; display: flex; }
  .color-band span { flex: 1; }
</style>
</head>
<body>

<section class="card card--back" aria-label="Card back">
  <div class="back-header">
    <span class="tagline">The way you are</span>
    <span class="header-divider"></span>
    <span class="brand-small">Novra</span>
  </div>
  <div class="stat">
    <p class="stat-figure">63%</p>
    <p class="stat-text">Of consumer value<br>privacy over popularity<br>when dealing with<br>online platform</p>
  </div>
  <p class="source">Survey, Meridian Daily</p>
</section>

<section class="card card--front" aria-label="Card front">
  <div class="tech-artwork" role="img" aria-label="Decorative concentric tech ring artwork in teal and blue"></div>

  <p class="brand-large">Novra</p>

  <div class="rule rule--teal"></div>
  <div class="rule rule--blue"></div>

  <ul class="contacts">
    <li class="contact">
      <span class="contact-icon">
        <svg width="12" height="12" viewBox="0 0 24 24" aria-hidden="true"><path fill="#fff" d="M6.6 10.8a15 15 0 0 0 6.6 6.6l2.2-2.2a1 1 0 0 1 1-.25 11.4 11.4 0 0 0 3.6.57 1 1 0 0 1 1 1V20a1 1 0 0 1-1 1A17 17 0 0 1 3 4a1 1 0 0 1 1-1h3.5a1 1 0 0 1 1 1c0 1.25.2 2.45.57 3.6a1 1 0 0 1-.25 1z"/></svg>
      </span>
      555-013-4821
    </li>
    <li class="contact">
      <span class="contact-icon">
        <svg width="12" height="10" viewBox="0 0 24 18" aria-hidden="true"><rect x="1" y="1" width="22" height="16" fill="none" stroke="#fff" stroke-width="2"/><path d="M1 1l11 9 11-9" fill="none" stroke="#fff" stroke-width="2"/></svg>
      </span>
      daniel@novrahq.com
    </li>
  </ul>

  <div class="identity">
    <p class="person-name">DANIEL REYES</p>
    <p class="person-role">CEO/FOUNDER</p>
  </div>

  <div class="color-band">
    <span style="background: var(--blue-mid)"></span>
    <span style="background: var(--blue-deep)"></span>
    <span style="background: var(--blue)"></span>
    <span style="background: var(--teal-light)"></span>
    <span style="background: var(--teal)"></span>
    <span style="background: var(--teal-light)"></span>
  </div>
</section>

</body>
</html>
```